"MEET THE TEAM" page web design

We need a "meet the team" page for our website!
Please look at our website to see the style we need

We are looking for something unique, fun, cool, technology-style and yet professional. We plan on taking a picture of each employee (not sure if this will be a real photo/caricature/ black and white/goofy picture--> but we are open to any ideas you have that will work with the design) and putting it there, along with a little bio about each person.

Thanks! looking forward to working together:)
Updates

Project Deadline Extended
Reason: I am excited to see more designs and find the perfect fit. Thanks designers :)

Target Market(s)

People looking to purchase servers, workstations, components

Industry/Entity Type

Information Technology

Number of Pages Required

1 page

Font styles to use
Sans Serif
Other font styles liked:
• The font we use on our site so it matches

Requirements
Must have
• please look at our website quenditrex.com and see the theme and colors we want.
• We have 13 employees but would like to have a design where we can add/remove people if we hire/terminate them without messing up the design.
• We are looking for something unique, fun, cool, technology-style and yet professional. We plan on taking a picture of each employee (not sure if this will be a real photo/caricature/ black and white/goofy picture--> but we are open to any ideas you have that will work with the design) and putting it there, along with a little bio about each person.
• We can upload anything you need
Nice to have
• We are also interested in having a design where when the cursor moves over a person then the bio comes out or moves around, or something. (This is not required, but we would love some cool ideas) And if you can come up with some design, we would have our programmers create it for us.
Should not have
• we are open to anything

```html
<!DOCTYPE html>
<html lang="en">
<head>
<meta charset="utf-8">
<title>Meet the Team – Quenditrex</title>
<link href="https://fonts.googleapis.com/css2?family=Open+Sans:wght@300;400;600;700&family=Roboto:wght@300;400&display=swap" rel="stylesheet">
<style>
:root{
  --teal:#17b9a8;
  --teal-dark:#12978a;
  --ink:#333333;
  --panel-light:#e4e4e4;
  --panel-dark:#c2c2c2;
  --footer:#a7a7a7;
  --footer-deep:#9b9b9b;
  --white:#ffffff;
}
*{box-sizing:border-box;margin:0;padding:0}
html,body{width:860px;height:1200px;overflow:hidden}
body{position:relative;background:var(--white);font-family:"Open Sans",sans-serif;color:var(--ink)}

/* header */
.site-header{position:absolute;left:0;top:0;width:860px;height:74px;background:var(--white);border-bottom:1px solid #ddd}
.brand{position:absolute;left:46px;top:17px;display:flex;align-items:center;gap:10px}
.brand-dot{width:34px;height:34px;border-radius:50%;background:var(--teal)}
.brand-name{font-family:"Open Sans",sans-serif;font-weight:400;font-size:24px;color:var(--teal)}
.account-tab{position:absolute;left:678px;top:0;width:139px;height:24px;border-radius:0 0 16px 16px;overflow:hidden;display:flex;font-size:8px}
.account-tab span{flex:1;display:flex;align-items:center;justify-content:center;color:#555}
.account-tab .signup{background:#c8c8c8}
.account-tab .login{background:#9d9d9d;color:#eee}
.contact-bubble{position:absolute;width:30px;height:30px;border-radius:50%;border:1px solid #ccc;display:flex;align-items:center;justify-content:center}
.live-chat-label{position:absolute;left:636px;top:45px;font-size:10px;color:#555}
.header-phone{position:absolute;left:737px;top:41px;font-size:14px;color:#333}

.main-nav{position:absolute;left:0;top:74px;width:860px;height:35px;background:var(--white)}
.main-nav ul{list-style:none;position:absolute;left:44px;top:10px;display:flex}
.main-nav li{font-size:8.3px;color:#444;letter-spacing:.2px;margin-right:19px}
.main-nav li:last-child{margin-right:0}
.search-box{position:absolute;left:667px;top:7px;width:119px;height:24px;border:1px solid #bbb;border-radius:12px;font-size:8px;color:#444;padding:7px 0 0 15px}
.search-box svg{position:absolute;right:8px;top:5px}
.cart-button{position:absolute;left:792px;top:6px;width:28px;height:28px;border-radius:50%;border:1px solid #bbb;display:flex;align-items:center;justify-content:center}

/* title band */
.page-title{position:absolute;left:0;top:109px;width:860px;height:39px;background:var(--teal);color:var(--white);font-family:"Roboto",sans-serif;font-weight:300;font-size:23px;text-align:center;line-height:39px;letter-spacing:.5px}
.page-title::after{content:"";position:absolute;left:420px;top:39px;border:10px solid transparent;border-top:9px solid var(--teal);z-index:3}

/* team rows */
.member{position:absolute;left:0;width:860px;height:226px;border-bottom:1px solid #e8e8e8}
.member.photo-left{background:radial-gradient(ellipse at 35% 40%,var(--panel-light),#d3d3d3 55%,var(--panel-dark))}
.member.photo-right{background:radial-gradient(ellipse at 75% 40%,var(--panel-light),#d3d3d3 55%,var(--panel-dark))}
.member-photo{position:absolute;bottom:0;border-radius:60px 60px 0 0}
.member-name{position:absolute;font-weight:300;font-size:22px;color:var(--teal-dark)}
.member-role{position:absolute;font-size:12px;color:#333;letter-spacing:.4px}
.member-bio{position:absolute;width:467px;font-size:10.2px;line-height:13px;color:#333;text-align:justify}
.member-links{position:absolute;display:flex;gap:22px;align-items:center}

/* footer */
.site-footer{position:absolute;left:0;top:825px;width:860px;height:240px;background:var(--footer);color:var(--white)}
.footer-about{position:absolute;left:200px;top:7px;width:422px;font-family:Arial,sans-serif;font-size:12.5px;line-height:15.5px;text-align:center}
.footer-rule{position:absolute;height:1px;background:linear-gradient(90deg,transparent,#d6d6d6,transparent)}
.footer-contact{position:absolute;top:113px;font-family:Arial,sans-serif;font-size:12.5px;line-height:16px}
.footer-contact svg{position:absolute;left:-18px;top:1px}
.footer-col{position:absolute;top:158px;font-family:Arial,sans-serif;font-size:14px}
.support-links{position:absolute;left:526px;top:180px;width:90px;text-align:center;font-family:Arial,sans-serif;font-weight:700;font-size:8px;line-height:11.3px}
.footer-base{position:absolute;left:0;top:1065px;width:860px;height:135px;background:var(--footer-deep);color:var(--white)}
.social{position:absolute;top:16px;width:30px;height:30px;border-radius:50%;border:1px solid #d4d4d4}
.social::after{content:"";position:absolute;left:11px;top:11px;width:7px;height:7px;border-radius:50%;background:#e2e2e2}
.legal{position:absolute;left:347px;top:75px;font-family:Arial,sans-serif;font-size:11px;line-height:14.5px;display:flex;gap:8px}
.legal-mark{width:18px;height:18px;background:#e4e4e4;margin-top:4px}
.chat-now{position:absolute;left:680px;top:1184px;width:168px;height:20px;background:var(--teal);border-radius:5px 5px 0 0;color:var(--white);font-size:10.5px;font-weight:700;padding:4px 0 0 8px;border:1px solid #fff}
</style>
</head>
<body>

<header class="site-header">
  <div class="brand">
    <div class="brand-dot"></div>
    <div class="brand-name">Quenditrex</div>
  </div>
  <div class="account-tab"><span class="signup">SIGN UP</span><span class="login">LOGIN</span></div>
  <div class="contact-bubble" style="left:598px;top:34px">
    <svg width="12" height="10" viewBox="0 0 12 10"><path d="M1 1h10v6H5l-3 2V7H1z" fill="var(--teal)"/></svg>
  </div>
  <div class="live-chat-label">LIVE CHAT</div>
  <div class="contact-bubble" style="left:697px;top:33px">
    <svg width="12" height="12" viewBox="0 0 24 24"><path d="M6.6 10.8a15 15 0 0 0 6.6 6.6l2.2-2.2c.3-.3.7-.4 1-.2 1.1.4 2.3.6 3.6.6.6 0 1 .4 1 1V20c0 .6-.4 1-1 1A17 17 0 0 1 3 4c0-.6.4-1 1-1h3.5c.6 0 1 .4 1 1 0 1.3.2 2.5.6 3.6.1.3 0 .7-.2 1z" fill="var(--teal)"/></svg>
  </div>
  <div class="header-phone">555-014-2290</div>
</header>

<nav class="main-nav">
  <ul>
    <li>SERVERS</li>
    <li>WORKSTATIONS</li>
    <li>COMPONENTS</li>
    <li>VIRTUAL REALITY</li>
    <li>DRONES</li>
    <li>ABOUT US</li>
    <li>BLOG</li>
    <li>RESOURCES</li>
    <li>CONTACT US</li>
  </ul>
  <div class="search-box">Search
    <svg width="12" height="12" viewBox="0 0 12 12"><circle cx="5" cy="5" r="3.6" fill="none" stroke="var(--teal)" stroke-width="1.6"/><path d="M7.6 7.6l3 3" stroke="var(--teal)" stroke-width="1.8"/></svg>
  </div>
  <div class="cart-button">
    <svg width="14" height="12" viewBox="0 0 14 12"><path d="M1 4h12l-1.5 7h-9z" fill="var(--teal)"/><path d="M4 4l2-3M10 4L8 1" stroke="var(--teal)" stroke-width="1.2"/></svg>
  </div>
</nav>

<h1 class="page-title">MEET THE TEAM</h1>

<main>
  <section class="member photo-left" style="top:148px">
    <div class="member-photo" role="img" aria-label="Portrait of developer, arms crossed, light blue shirt" style="left:90px;width:165px;height:212px;background:linear-gradient(180deg,#9aa0a6 0%,#b9c6d4 40%,#8fa2b8 100%)"></div>
    <h2 class="member-name" style="left:314px;top:15px">Daren Colm</h2>
    <p class="member-role" style="left:316px;top:49px">DEVELOPER</p>
    <p class="member-bio" style="left:314px;top:70px">Lorem ipsum dolor sit amet, consectetuer adipiscing elit, sed diam nonummy nibh euismod tincidunt ut laoreet dolore magna aliquam erat volutpat. Ut wisi enim ad minim veniam, quis nostrud exerci tation ullamcorper suscipit lobortis nisl ut aliquip ex ea commodo consequat. Duis autem vel eum iriure dolor in hendrerit in vulputate velit esse molestie consequat, vel illum dolore eu feugiat nulla facilisis at vero eros et accumsan et iusto odio dignissim qui blandit praesent luptatum zzril delenit augue duis dolore te feugait nulla facilisis.</p>
    <div class="member-links" style="left:655px;top:202px">
      <svg width="12" height="12" viewBox="0 0 24 24"><path d="M6.6 10.8a15 15 0 0 0 6.6 6.6l2.2-2.2c.3-.3.7-.4 1-.2 1.1.4 2.3.6 3.6.6.6 0 1 .4 1 1V20c0 .6-.4 1-1 1A17 17 0 0 1 3 4c0-.6.4-1 1-1h3.5c.6 0 1 .4 1 1 0 1.3.2 2.5.6 3.6.1.3 0 .7-.2 1z" fill="#bbb"/></svg>
      <svg width="12" height="12" viewBox="0 0 12 12"><circle cx="6" cy="6" r="4" fill="var(--ink)"/></svg>
      <svg width="12" height="12" viewBox="0 0 12 12"><rect x="1.5" y="1.5" width="9" height="9" fill="var(--ink)"/></svg>
      <svg width="14" height="11" viewBox="0 0 14 11"><rect x="0.5" y="0.5" width="13" height="10" fill="var(--ink)"/><path d="M0.5 0.5l6.5 5 6.5-5" stroke="#d0d0d0" fill="none"/></svg>
    </div>
  </section>

  <section class="member photo-right" style="top:374px">
    <h2 class="member-name" style="left:86px;top:15px">Hugo Penn</h2>
    <p class="member-role" style="left:87px;top:49px">QC INCHARGE</p>
    <p class="member-bio" style="left:87px;top:71px">Lorem ipsum dolor sit amet, consectetuer adipiscing elit, sed diam nonummy nibh euismod tincidunt ut laoreet dolore magna aliquam erat volutpat. Ut wisi enim ad minim veniam, quis nostrud exerci tation ullamcorper suscipit lobortis nisl ut aliquip ex ea commodo consequat. Duis autem vel eum iriure dolor in hendrerit in vulputate velit esse molestie consequat, vel illum dolore eu feugiat nulla facilisis at vero eros et accumsan et iusto odio dignissim qui blandit praesent luptatum zzril delenit augue duis dolore te feugait nulla facilisis.</p>
    <div class="member-links" style="left:87px;top:197px">
      <svg width="12" height="12" viewBox="0 0 24 24"><path d="M6.6 10.8a15 15 0 0 0 6.6 6.6l2.2-2.2c.3-.3.7-.4 1-.2 1.1.4 2.3.6 3.6.6.6 0 1 .4 1 1V20c0 .6-.4 1-1 1A17 17 0 0 1 3 4c0-.6.4-1 1-1h3.5c.6 0 1 .4 1 1 0 1.3.2 2.5.6 3.6.1.3 0 .7-.2 1z" fill="var(--ink)"/></svg>
      <svg width="12" height="12" viewBox="0 0 12 12"><circle cx="6" cy="6" r="4" fill="var(--ink)"/></svg>
      <svg width="12" height="12" viewBox="0 0 12 12"><rect x="1.5" y="1.5" width="9" height="9" fill="var(--ink)"/></svg>
      <svg width="14" height="11" viewBox="0 0 14 11"><rect x="0.5" y="0.5" width="13" height="10" fill="var(--ink)"/><path d="M0.5 0.5l6.5 5 6.5-5" stroke="#d0d0d0" fill="none"/></svg>
    </div>
    <div class="member-photo" role="img" aria-label="Portrait of QC lead, arms crossed, dark grey t-shirt" style="left:612px;width:122px;height:210px;background:linear-gradient(180deg,#8a7a70 0%,#555 45%,#3a3a3a 100%)"></div>
  </section>

  <section class="member photo-left" style="top:600px">
    <div class="member-photo" role="img" aria-label="Portrait of design head, arms crossed, grey blazer" style="left:86px;width:155px;height:205px;background:linear-gradient(180deg,#6b5144 0%,#a79f99 40%,#8e8985 100%)"></div>
    <h2 class="member-name" style="left:312px;top:16px">Mira Salt</h2>
    <p class="member-role" style="left:313px;top:51px">Design Head</p>
    <p class="member-bio" style="left:314px;top:73px">Lorem ipsum dolor sit amet, consectetuer adipiscing elit, sed diam nonummy nibh euismod tincidunt ut laoreet dolore magna aliquam erat volutpat. Ut wisi enim ad minim veniam, quis nostrud exerci tation ullamcorper suscipit lobortis nisl ut aliquip ex ea commodo consequat. Duis autem vel eum iriure dolor in hendrerit in vulputate velit esse molestie consequat, vel illum dolore eu feugiat nulla facilisis at vero eros et accumsan et iusto odio dignissim qui blandit praesent luptatum zzril delenit augue duis dolore te feugait nulla facilisis.</p>
    <div class="member-links" style="left:655px;top:202px">
      <svg width="12" height="12" viewBox="0 0 24 24"><path d="M6.6 10.8a15 15 0 0 0 6.6 6.6l2.2-2.2c.3-.3.7-.4 1-.2 1.1.4 2.3.6 3.6.6.6 0 1 .4 1 1V20c0 .6-.4 1-1 1A17 17 0 0 1 3 4c0-.6.4-1 1-1h3.5c.6 0 1 .4 1 1 0 1.3.2 2.5.6 3.6.1.3 0 .7-.2 1z" fill="var(--ink)"/></svg>
      <svg width="12" height="12" viewBox="0 0 12 12"><circle cx="6" cy="6" r="4" fill="var(--ink)"/></svg>
      <svg width="12" height="12" viewBox="0 0 12 12"><rect x="1.5" y="1.5" width="9" height="9" fill="var(--ink)"/></svg>
      <svg width="14" height="11" viewBox="0 0 14 11"><rect x="0.5" y="0.5" width="13" height="10" fill="var(--ink)"/><path d="M0.5 0.5l6.5 5 6.5-5" stroke="#d0d0d0" fill="none"/></svg>
    </div>
  </section>
</main>

<footer class="site-footer">
  <p class="footer-about">Based in Fenwick Park California, Quenditrex offers custom servers, storage, and workstations for local businesses in Los Angeles, Beverly Hills, Thousand Oaks, Ventura, Orange County, Santa Barbara, Oxnard, Irvine, Anaheim, and San Diego. Quenditrex also offers such products to clients throughout the United States and Worldwide.</p>
  <div class="footer-rule" style="left:195px;top:83px;width:450px"></div>
  <div class="footer-contact" style="left:221px">
    <svg width="10" height="13" viewBox="0 0 10 13"><path d="M5 0a4.5 4.5 0 0 1 4.5 4.5C9.5 8 5 13 5 13S.5 8 .5 4.5A4.5 4.5 0 0 1 5 0z" fill="#fff"/><circle cx="5" cy="4.5" r="1.6" fill="var(--footer)"/></svg>
    4182 Marlow Ave.<br>Fenwick Park, CA 90120
  </div>
  <div class="footer-contact" style="left:365px">
    <svg width="12" height="12" viewBox="0 0 24 24"><path d="M6.6 10.8a15 15 0 0 0 6.6 6.6l2.2-2.2c.3-.3.7-.4 1-.2 1.1.4 2.3.6 3.6.6.6 0 1 .4 1 1V20c0 .6-.4 1-1 1A17 17 0 0 1 3 4c0-.6.4-1 1-1h3.5c.6 0 1 .4 1 1 0 1.3.2 2.5.6 3.6.1.3 0 .7-.2 1z" fill="#fff"/></svg>
    555-014-2290
  </div>
  <div class="footer-contact" style="left:493px">
    <svg width="13" height="10" viewBox="0 0 13 10"><rect width="13" height="10" fill="#fff"/><path d="M0 0l6.5 5L13 0" stroke="var(--footer)" fill="none"/></svg>
    sales@quenditrex.com
  </div>
  <div class="footer-col" style="left:176px">Computers</div>
  <div class="footer-col" style="left:283px">Drones</div>
  <div class="footer-col" style="left:360px">Virtual</div>
  <div class="footer-col" style="left:448px">About</div>
  <div class="footer-col" style="left:517px">Customer Support</div>
  <div class="support-links">Terms and<br>Conditions<br>Warranty Information<br>Contact Us<br>Return Policy</div>
</footer>

<div class="footer-base">
  <div class="social" style="left:302px" aria-label="Social profile"></div>
  <div class="social" style="left:344px" aria-label="Social profile"></div>
  <div class="social" style="left:386px" aria-label="Social profile"></div>
  <div class="social" style="left:429px" aria-label="Social profile"></div>
  <div class="footer-rule" style="left:50px;top:63px;width:710px"></div>
  <div class="legal"><div class="legal-mark"></div><div>Quenditrex, LLC.<br>Copyright © 2017</div></div>
</div>

<div class="chat-now">CHAT NOW</div>

</body>
</html>
```